Menu Design Project

We trying to replace old flyer/menu with some new design.
hello this is my old menu i attached in email and my logo, the text you can pick from the menu and and i also attached some new picture for the food ,with my menu size unfold. front and back and then fold to 3.5" * 11". please show me what best can you do .Trifold is fine but must have image of food,
this is indian Restaurant
thats fine to have trifold menu design do to short time

Need to add also food picture on menu

Font styles to use
Serif
Decorative
Script

Colors

Designer to choose colors to be used in the design.

Requirements
Must have
• food image on menu
• trifold is fine ( do to short time)
• menu has to elegant ,color or text can be optional, Menu need to be neat and clean no too much rush on between the words .

```html
<!DOCTYPE html>
<html lang="en">
<head>
<meta charset="utf-8">
<title>Saffron Court Palace — Menu</title>
<link href="https://fonts.googleapis.com/css2?family=Oswald:wght@300;400&family=Josefin+Sans:wght@400;600&family=Cormorant+Garamond:wght@600&display=swap" rel="stylesheet">
<style>
:root{
  --navy:#1c2849;
  --ink:#0a0a0c;
  --gold:#f1d23a;
  --white:#ffffff;
  --muted:#cfcfcf;
}
*{margin:0;padding:0;box-sizing:border-box}
html,body{width:1145px;height:1200px;overflow:hidden;background:var(--navy)}
.menu{position:relative;width:1145px;height:1200px;background:var(--navy);font-family:"Oswald",sans-serif;color:var(--white)}
.panel{position:absolute}
.arch{left:24px;top:40px;width:334px;height:1160px;background:var(--ink);border-radius:167px 167px 0 0/70px 70px 0 0}
.center{left:382px;top:0;width:381px;height:994px;background:var(--ink)}
.heading{position:absolute;left:0;width:100%;text-align:center;color:var(--gold);font-weight:400;font-size:22px;line-height:1;letter-spacing:.5px}
.flourish{position:absolute;left:50%;transform:translateX(-50%);width:40px;height:6px}
.list{position:absolute;list-style:none}
.item{display:flex;flex-direction:column}
.row{display:flex;align-items:baseline;font-weight:300;font-size:11px;color:var(--gold);text-transform:uppercase;line-height:1.2}
.lead{flex:1;border-bottom:2px dotted var(--gold);margin:0 4px;transform:translateY(-3px);opacity:.9}
.desc{font-family:"Josefin Sans",sans-serif;font-size:6px;color:var(--muted);padding-left:8px;line-height:1.4}
.photo{position:absolute}
.photo-hall{left:763px;top:0;width:382px;height:216px;background:linear-gradient(100deg,#c9a86a,#8a3a2e 55%,#d9c3a1)}
.photo-food{left:382px;top:994px;width:381px;height:206px;background:radial-gradient(circle at 55% 45%,#f0e6c8 0,#d99a3a 35%,#9a5a1c 80%)}
.notes{position:absolute;left:392px;top:1160px;font-family:"Josefin Sans",sans-serif;font-size:10px;color:var(--white);line-height:1.7}
.badge{position:absolute;left:786px;top:150px;width:336px;height:288px;background:var(--white);border-radius:40px;display:flex;flex-direction:column;align-items:center;justify-content:flex-end;padding-bottom:40px;color:#111}
.badge-mark{width:70px;height:70px;border-radius:50%;border:2px solid #111;margin-bottom:22px}
.brand{font-family:"Josefin Sans",sans-serif;font-weight:400;font-size:25px}
.brand-sub{font-family:"Cormorant Garamond",serif;font-weight:600;font-size:17px;color:#d8b526;margin-top:8px}
.brand-rule{width:210px;height:1px;background:#111;margin:12px 0 10px}
.brand-tag{font-family:"Josefin Sans",sans-serif;font-size:12px}
.services{position:absolute;left:763px;top:462px;width:382px;text-align:center;color:var(--gold);font-size:37px;line-height:1.2;font-weight:400}
.hours{position:absolute;left:812px;top:592px;width:280px;height:350px;background:var(--ink);border-radius:26px;text-align:center;font-family:"Josefin Sans",sans-serif}
.hours h3{color:var(--gold);font-weight:400;font-size:18px;margin-top:48px}
.hours p{font-size:13px;line-height:1.55;margin-top:20px}
.hours hr{border:0;border-top:1px solid var(--muted);width:200px;margin:40px auto 0}
.hours h3.lunch{margin-top:34px}
.contact{position:absolute;left:763px;top:1014px;width:382px;text-align:center;font-family:"Josefin Sans",sans-serif;font-size:14px;line-height:27px;font-style:normal}
.pin{display:inline-block;vertical-align:-2px;margin-right:8px}
</style>
</head>
<body>
<main class="menu">

  <section class="panel arch" aria-label="Vegetarian and rice">
    <h2 class="heading" style="top:40px">HANDI SE<br>(VEGETARIAN)</h2>
    <svg class="flourish" style="top:104px" viewBox="0 0 40 6"><path d="M0 3h15M25 3h15" stroke="#fff" stroke-width="1"/><circle cx="20" cy="3" r="2.5" fill="none" stroke="#fff"/></svg>
    <ul class="list" style="left:25px;top:130px;width:300px">
      <li class="item" style="height:27.3px"><div class="row">Paneer Makhni<span class="lead"></span>$8.99</div><div class="desc">fresh home made cheese folded into creamy tomato sauce</div></li>
      <li class="item" style="height:27.3px"><div class="row">Paneer Tikka Masala<span class="lead"></span>$8.99</div><div class="desc">cottage cheese sauteed with bell pepper, onion folded into a spiced tomato sauce</div></li>
      <li class="item" style="height:27.3px"><div class="row">Kadai Paneer<span class="lead"></span>$8.99</div><div class="desc">fresh home made cubes of cheese stir fry in a kadai with onion, ginger, tomato, and bell pepper</div></li>
      <li class="item" style="height:27.3px"><div class="row">Palak Paneer<span class="lead"></span>$8.99</div><div class="desc">fresh spinach cooked with cubes of cheese and seasoned with garlic</div></li>
      <li class="item" style="height:27.3px"><div class="row">Mutter Paneer<span class="lead"></span>$8.49</div><div class="desc">home made cheese cooked with green peas in a mildly spiced sauce</div></li>
      <li class="item" style="height:27.3px"><div class="row">Shahi Paneer<span class="lead"></span>$8.99</div><div class="desc">paneer cubes cooked in a rich creamy almond sauce</div></li>
      <li class="item" style="height:27.3px"><div class="row">Paneer Bhurji<span class="lead"></span>$10.99</div><div class="desc">fresh home made cheese grated and cooked with green pepper, tomato &amp; onions</div></li>
      <li class="item" style="height:27.3px"><div class="row">Malai Kofta<span class="lead"></span>$8.99</div><div class="desc">cheese vegetable balls in a savory almond flavored creamy sauce</div></li>
      <li class="item" style="height:27.3px"><div class="row">Navratan Korma<span class="lead"></span>$8.99</div><div class="desc">combination of italian vegetable, cooked in a cashew &amp; almond sauce</div></li>
      <li class="item" style="height:27.3px"><div class="row">Kaju Mushroom Mutter<span class="lead"></span>$9.29</div><div class="desc">fresh mushroom, cashew, peas cooked in onion and cashew sauce</div></li>
      <li class="item" style="height:27.3px"><div class="row">Methi Malai Mutter<span class="lead"></span>$9.29</div><div class="desc">fenugreek leaves cooked with peas in a cashew flavor lightly cream sauce</div></li>
      <li class="item" style="height:27.3px"><div class="row">Aloo Gobhi<span class="lead"></span>$8.50</div><div class="desc">a dry Indian dish made with potatoes, cauliflower, &amp; ginger</div></li>
      <li class="item" style="height:27.3px"><div class="row">Bhindi Masala<span class="lead"></span>$8.50</div><div class="desc">fresh okra sauteed with brown onion &amp; tomatoes</div></li>
      <li class="item" style="height:27.3px"><div class="row">Achari Baigan<span class="lead"></span>$8.49</div><div class="desc">baby eggplant cooked in spicy picklish flavor masala</div></li>
      <li class="item" style="height:27.3px"><div class="row">Baigan Bharta<span class="lead"></span>$8.49</div><div class="desc">eggplant roasted on charcoal, minced and cooked with onions &amp; tomatoes</div></li>
      <li class="item" style="height:27.3px"><div class="row">Vegetable Jalfrezi<span class="lead"></span>$8.49</div><div class="desc">mixed vegetable with cottage cheese mildly spiced</div></li>
      <li class="item" style="height:27.3px"><div class="row">Zeera Aloo<span class="lead"></span>$7.50</div><div class="desc">crispy potato stir fry with cumin seeds</div></li>
      <li class="item" style="height:27.3px"><div class="row">Sarson Ka Saag<span class="lead"></span>$8.49</div><div class="desc">mustard leaves cooked in a Punjabi style tastes really nice with makki ki roti</div></li>
      <li class="item" style="height:27.3px"><div class="row">Chana Peshawari<span class="lead"></span>$8.49</div><div class="desc">delicious chickpeas cooked in an exotic blend of North Indian spices</div></li>
      <li class="item" style="height:27.3px"><div class="row">Chana Palak<span class="lead"></span>$8.49</div><div class="desc">frontier chick peas cooked with fresh spinach</div></li>
      <li class="item" style="height:27.3px"><div class="row">Punjabi Kadi<span class="lead"></span>$8.49</div><div class="desc">a stew made with yogurt &amp; chickpeas flour seasoned with spices</div></li>
      <li class="item" style="height:27.3px"><div class="row">Daal Tarka Yellow<span class="lead"></span>$8.49</div><div class="desc">slow simmered yellow lentils sauteed with tomato, ginger, and garlic</div></li>
      <li class="item" style="height:27.3px"><div class="row">Daal Tarka Black<span class="lead"></span>$8.49</div><div class="desc">slow simmered black lentils sauteed with tomato, ginger, and garlic</div></li>
      <li class="item" style="height:27.3px"><div class="row">Daal Makhni<span class="lead"></span>$8.49</div><div class="desc">classic lentils with kidney beans simmered in tomato &amp; light butter</div></li>
    </ul>

    <h2 class="heading" style="top:816px">BIRYANI &amp; RICE</h2>
    <svg class="flourish" style="top:856px" viewBox="0 0 40 6"><path d="M0 3h15M25 3h15" stroke="#fff" stroke-width="1"/><circle cx="20" cy="3" r="2.5" fill="none" stroke="#fff"/></svg>
    <ul class="list" style="left:25px;top:884px;width:300px">
      <li class="item" style="height:27.4px"><div class="row">Chicken Biryani<span class="lead"></span>$7.99</div><div class="desc">boneless chicken cooked on low heat with long grain basmati rice</div></li>
      <li class="item" style="height:27.4px"><div class="row">Goat Biryani<span class="lead"></span>$9.50</div><div class="desc">goat cooked on low heat with long grain basmati rice</div></li>
      <li class="item" style="height:27.4px"><div class="row">Lamb Biryani<span class="lead"></span>$9.99</div><div class="desc">lamb cooked on low heat with long grain basmati rice</div></li>
      <li class="item" style="height:27.4px"><div class="row">Shrimp Biryani<span class="lead"></span>$10.99</div><div class="desc">shrimp cooked on low heat with long grain basmati rice</div></li>
      <li class="item" style="height:27.4px"><div class="row">Vegetable Biryani<span class="lead"></span>$7.50</div><div class="desc">basmati rice cooked with mixed vegetable in a blend of herbs nuts and saffron</div></li>
      <li class="item" style="height:27.4px"><div class="row">Zeera Rice<span class="lead"></span>$3.99</div><div class="desc"></div></li>
      <li class="item" style="height:27.4px"><div class="row">Peas Pulao<span class="lead"></span>$6.99</div><div class="desc"></div></li>
      <li class="item" style="height:40px"><div class="row">Royal Spl Biryani<span class="lead"></span>$11.99</div><div class="desc">long basmati rice flavored with saffron then sauteed together with shrimp, quality lamb and pieces of chicken in delicate blend of spices and nut</div></li>
    </ul>
  </section>

  <section class="panel center" aria-label="Breads, desserts and beverages">
    <h2 class="heading" style="top:26px">TANDOORI BREAD</h2>
    <ul class="list" style="left:52px;top:94px;width:290px">
      <li class="item" style="height:27.4px"><div class="row">Tandoori Roti<span class="lead"></span>$1.75</div><div class="desc">flat whole wheat bread baked in a clay oven</div></li>
      <li class="item" style="height:27.4px"><div class="row">Tandoori Naan<span class="lead"></span>$1.75</div><div class="desc">soft white bread baked in a clay oven</div></li>
      <li class="item" style="height:27.4px"><div class="row">Garlic Naan<span class="lead"></span>$2.50</div><div class="desc">naan flavored with fresh garlic and butter</div></li>
      <li class="item" style="height:27.4px"><div class="row">Lachha Paratha<span class="lead"></span>$2.50</div><div class="desc">rich multilayered whole wheat bread baked in clay oven</div></li>
      <li class="item" style="height:27.4px"><div class="row">Onion Kulcha<span class="lead"></span>$2.99</div><div class="desc">naan bread stuffed with seasoned finely chopped onions</div></li>
      <li class="item" style="height:27.4px"><div class="row">Aloo Paratha<span class="lead"></span>$2.99</div><div class="desc">whole wheat paratha stuffed with mildly spice mashed potato</div></li>
      <li class="item" style="height:27.4px"><div class="row">Gobhi Paratha<span class="lead"></span>$3.50</div><div class="desc">wheat bread stuffed with mildly spiced cauliflower</div></li>
      <li class="item" style="height:27.4px"><div class="row">Pudina Paratha<span class="lead"></span>$2.99</div><div class="desc">tandoori paratha flavored with fresh mint</div></li>
      <li class="item" style="height:27.4px"><div class="row">Keema Naan<span class="lead"></span>$3.99</div><div class="desc">whole wheat bread stuffed with fresh chicken keema</div></li>
      <li class="item" style="height:27.4px"><div class="row">Jalebi Paratha<span class="lead"></span>$2.99</div><div class="desc">rich multi-layered naan bread</div></li>
    </ul>

    <h2 class="heading" style="top:388px">DESSERTS</h2>
    <ul class="list" style="left:52px;top:458px;width:290px">
      <li class="item" style="height:27.6px"><div class="row">Kheer<span class="lead"></span>$3.99</div><div class="desc">basmati rice pudding flavored with cardamom, nuts, raisins and topped with pistachio</div></li>
      <li class="item" style="height:27.6px"><div class="row">Rasmalai<span class="lead"></span>$3.99</div><div class="desc">2pcs of cold cheese dumpling flavored with cardamom, saffron and topped with lightly sweet milk syrup</div></li>
      <li class="item" style="height:27.6px"><div class="row">Gajar Halwa<span class="lead"></span>$3.99</div><div class="desc">fresh carrot cooked with milk cottage, cheese and nuts</div></li>
      <li class="item" style="height:27.6px"><div class="row">Gulab Jamun<span class="lead"></span>$3.99</div><div class="desc">2pcs of golden fried balls of milk pastry soaked in honey syrup topped with shredded coconut</div></li>
      <li class="item" style="height:27.6px"><div class="row">Ice Cream<span class="lead"></span>$3.50</div><div class="desc">mango or vanilla or chocolate flavor</div></li>
    </ul>

    <h2 class="heading" style="top:614px">BEVERAGES</h2>
    <svg class="flourish" style="top:654px" viewBox="0 0 40 6"><path d="M0 3h15M25 3h15" stroke="#fff" stroke-width="1"/><circle cx="20" cy="3" r="2.5" fill="none" stroke="#fff"/></svg>
    <ul class="list" style="left:52px;top:682px;width:290px">
      <li class="item" style="height:27.4px"><div class="row">Mango Lassi<span class="lead"></span>$3.50</div><div class="desc">a refreshing yogurt mango drink</div></li>
      <li class="item" style="height:27.4px"><div class="row">Lassi<span class="lead"></span>$3.50</div><div class="desc">sweet or salted, a delicious yogurt drink</div></li>
      <li class="item" style="height:27.4px"><div class="row">Fresh Lemonade<span class="lead"></span>$2.99</div><div class="desc">a sweet and sour lemon flavor drink</div></li>
      <li class="item" style="height:27.4px"><div class="row">Pina Colada Virgin<span class="lead"></span>$3.99</div><div class="desc">combination of pineapple juice and coconut cream</div></li>
      <li class="item" style="height:27.4px"><div class="row">Strawberry Daiquiri Virgin<span class="lead"></span>$3.99</div><div class="desc">an ambrosial blend of ice strawberries and citrus soda, excellent on a hot summer day</div></li>
      <li class="item" style="height:27.4px"><div class="row">Juice<span class="lead"></span>$2.99</div><div class="desc">Orange juice • Pineapple juice • Mango juice</div></li>
      <li class="item" style="height:27.4px"><div class="row">Masala Tea<span class="lead"></span>$1.99</div><div class="desc">Indian tea with a mixture of aromatic Indian spice and herbs</div></li>
      <li class="item" style="height:27.4px"><div class="row">Cold Beers</div><div class="desc">Lager • Light Lager • Pilsner • Pale Ale • Amber and more...</div></li>
      <li class="item" style="height:27.4px"><div class="row">Wines<span class="lead"></span>$22.00 / $38.00</div><div class="desc">750 ml or 1.5 litre | Merlot • Cabernet • Chardonnay • Pinot Grigorio</div></li>
      <li class="item" style="height:16.5px"><div class="row">Cola, Lemon-Lime, Ginger Ale<span class="lead"></span>$1.50</div></li>
      <li class="item" style="height:16.5px"><div class="row">Indian Beers<span class="lead"></span>$12.99</div></li>
      <li class="item" style="height:16.5px"><div class="row">Coffee<span class="lead"></span>$1.99</div></li>
    </ul>
  </section>

  <div class="photo photo-hall" role="img" aria-label="Photo of the restaurant dining hall with booths and red chairs"></div>
  <div class="photo photo-food" role="img" aria-label="Photo of golden fried paneer pakoras stuffed with green chutney"></div>
  <p class="notes">*PRICES ARE SUBJECT TO CHANGE WITHOUT NOTICE<br>*TAX IS NOT INCLUDED IN THESE PRICES</p>

  <div class="badge">
    <div class="badge-mark"></div>
    <div class="brand">Saffron Court Palace</div>
    <div class="brand-sub">Restaurant and Banquet Hall</div>
    <div class="brand-rule"></div>
    <div class="brand-tag">THE BEST INDIAN CUISINE</div>
  </div>

  <p class="services">EAT IN • TAKE OUT<br>DELIVERY • CATERING</p>

  <div class="hours">
    <h3>BUSINESS HOURS:</h3>
    <p>SUN- THU 11:30AM - 12:00MN<br>FRI-SAT 11:30AM - 12:00MN</p>
    <hr>
    <h3 class="lunch">LUNCH SPECIAL</h3>
    <p>MON-SUN 11:30AM - 4:00PM</p>
  </div>

  <address class="contact">
    <div><svg class="pin" width="10" height="14" viewBox="0 0 10 14"><path d="M5 0a5 5 0 0 0-5 5c0 4 5 9 5 9s5-5 5-9a5 5 0 0 0-5-5z" fill="#f1d23a"/><circle cx="5" cy="5" r="2" fill="#1c2849"/></svg>240-15 HARBOR AVE., MAPLE HILL, NY 11500</div>
    <div>TEL: 555-210-4300 &nbsp; 555-210-4380</div>
    <div>FAX: 555-210-4392</div>
    <div>SAFFRONCOURTPALACE@MAILBOX.COM</div>
    <div>VISIT US AT WWW.SAFFRONCOURTPALACE.COM</div>
  </address>

</main>
</body>
</html>
```